Corvanta Business cards template

We're looking for something modern and elegant. We are a reseller of technology (computers, datacenter, etc). Color theme would be "only" white with the incorporation of the blue that's present on our website (Corvanta.com) and logo file. We would like for the card to provide all the necessary info for the specific person (Phone#, fax#, email, name, website URL) . I'm attaching the logo file to this request. Please have it show Montreal/New York somewhere, without providing specific addresses.

Target Market(s)

All b2b

Industry/Entity Type

Business

Contact Information for Business Card

Please have the color scheme be represented by only the white and blue from our website (Corvanta.com) and logo. We would like to logo on the card, but not big and overwhelming. This card will be used as a template for anybody within the company, it should display the user's name, phone#, fax#, email, job title and website URL. Please have it show Montreal/New York somewhere, without providing our specific addresses. Really, we're looking for a clean, simple and elegant look.

Font styles to use
Serif

Requirements
Must have
• Please see card details
Nice to have
• Please see card details
Should not have
• Anything tacky or tagline.

```html
<!DOCTYPE html>
<html lang="en">
<head>
<meta charset="utf-8">
<title>Corvanta Business Cards</title>
<link rel="stylesheet" href="https://fonts.googleapis.com/css2?family=Open+Sans:wght@400;600&display=swap">
<style>
  :root {
    --backdrop: #e6e8eb;
    --card-white: #ffffff;
    --brand-blue: #1c73bd;
    --brand-blue-light: #3d96d8;
    --text-gray: #4a4d52;
    --muted-gray: #6b6e73;
  }
  * { margin: 0; padding: 0; box-sizing: border-box; }
  html, body {
    width: 1200px; height: 960px; overflow: hidden;
    background: var(--backdrop);
    font-family: "Open Sans", Arial, sans-serif;
  }
  .sheet {
    position: relative; width: 1200px; height: 960px;
    display: flex; flex-direction: column; align-items: center; justify-content: center; gap: 60px;
  }
  .card {
    position: relative; width: 700px; height: 400px;
    background: var(--card-white);
    box-shadow: 0 6px 20px rgba(0,0,0,0.18);
    overflow: hidden;
  }
  .wordmark {
    color: var(--brand-blue);
    font-weight: 600;
    letter-spacing: 0.5px;
    line-height: 1;
  }
  /* Back */
  .card-back .wordmark {
    position: absolute; top: 150px; left: 0; width: 100%;
    text-align: center; font-size: 64px;
  }
  .card-back .site {
    position: absolute; top: 290px; left: 0; width: 100%;
    text-align: center; font-size: 15px; letter-spacing: 5px;
    color: var(--muted-gray);
  }
  /* Front */
  .card-front .swoosh { position: absolute; inset: 0; }
  .card-front .wordmark {
    position: absolute; top: 90px; left: 42px; font-size: 50px;
  }
  .holder {
    position: absolute; top: 118px; right: 40px; text-align: right; color: var(--card-white);
  }
  .holder .name { font-size: 20px; font-weight: 600; letter-spacing: 0.5px; }
  .holder .title { font-size: 17px; margin-top: 2px; }
  .contact {
    position: absolute; top: 205px; left: 42px;
    list-style: none; color: var(--text-gray); font-size: 16px; line-height: 1.55;
  }
  .contact .cities { margin-bottom: 8px; }
  .contact li { display: flex; align-items: center; gap: 8px; }
  .contact svg { width: 13px; height: 13px; fill: var(--brand-blue); flex: none; }
</style>
</head>
<body>
<main class="sheet">
  <section class="card card-back">
    <div class="wordmark">Corvanta</div>
    <div class="site">www.corvanta.com</div>
  </section>

  <section class="card card-front">
    <svg class="swoosh" viewBox="0 0 700 400" preserveAspectRatio="none">
      <rect width="700" height="400" fill="var(--brand-blue)"/>
      <path d="M0,48 C200,40 360,70 450,130 C540,200 555,310 470,375 L420,400 L0,400 Z" fill="var(--card-white)"/>
      <path d="M455,215 C525,280 505,350 360,383" fill="none" stroke="var(--brand-blue-light)" stroke-width="3"/>
      <path d="M440,215 C505,280 485,345 340,376" fill="none" stroke="var(--brand-blue)" stroke-width="1.5"/>
    </svg>
    <div class="wordmark">Corvanta</div>
    <div class="holder">
      <div class="name">DANIEL REYES</div>
      <div class="title">CEO/FOUNDER</div>
    </div>
    <ul class="contact">
      <li class="cities">Montreal/New York</li>
      <li><svg viewBox="0 0 16 16"><path d="M3 1h3l1 4-2 1c1 2 3 4 5 5l1-2 4 1v3c0 1-1 2-2 2C7 15 1 9 1 3c0-1 1-2 2-2z"/></svg>1-855-742-CORV (2678)</li>
      <li><svg viewBox="0 0 16 16"><path d="M4 1h7v4H4zM1 6h14v7h-3v2H4v-2H1zM5 10v4h6v-4z"/></svg>514 730 2285</li>
      <li><svg viewBox="0 0 16 16"><path d="M1 3h14v10H1zM2 4l6 5 6-5z" fill-rule="evenodd"/></svg>info@corvanta.com</li>
      <li><svg viewBox="0 0 16 16"><circle cx="8" cy="8" r="7"/></svg>www.corvanta.com</li>
    </ul>
  </section>
</main>
</body>
</html>
```